One page financial canvas needed

I am in the process of developing a financial planning process that uses a one page canvas as a tool for financial education and to explain simple and complex financial strategies to clients. I have the layout and content sorted, just need a hand making it look professional.

It should be a fairly simple project and i have attached a very rough hand drawn canvas showing the desired layout and content. Please feel free to be creative with the design keeping in mind this layout has been chosen to achieve certain outcomes.

Target Market(s)

25-45 Year old Homeowners who are interested in taking better care of the finances

Industry/Entity Type

Financial

Colors

Designer to choose colors to be used in the design.

Requirements
Must have
• very close to the layout in the attached file

```html
<!DOCTYPE html>
<html lang="en">
<head>
<meta charset="utf-8">
<title>Financial Planning Canvas</title>
<link rel="stylesheet" href="https://fonts.googleapis.com/css2?family=Source+Sans+3:wght@700&display=swap">
<style>
  :root {
    --blue: #00abe2;
    --orange: #f26125;
    --orange-ring: #f8c9a6;
    --income-tint: #e2eee5;
    --income-tint-low: #d5e6da;
    --expense-tint: #eeddd6;
    --expense-tint-low: #e2d2ce;
    --card-top: #fbfbfb;
    --card-bottom: #dcdcde;
    --white: #ffffff;
  }
  * { box-sizing: border-box; margin: 0; padding: 0; }
  html, body { width: 1200px; height: 776px; overflow: hidden; background: var(--white); }
  body { position: relative; font-family: "Source Sans 3", "Myriad Pro", Arial, sans-serif; font-weight: 700; }

  .canvas-card {
    position: absolute; left: 25px; top: 25px; width: 1133px; height: 697px;
    background: linear-gradient(to bottom, var(--card-top), var(--card-bottom));
    border-radius: 4px 4px 14px 14px;
    box-shadow: 0 6px 8px rgba(0,0,0,0.18);
  }
  .label {
    position: absolute; color: var(--white); font-size: 26px; letter-spacing: 1.2px;
    display: flex; align-items: center; justify-content: center; line-height: 1;
    padding-top: 3px; white-space: nowrap;
  }
  .tab-blue { background: var(--blue); height: 41px; border-radius: 3px 3px 0 0; }

  .goals-head { left: 25px; top: 25px; width: 260px; }
  .fears-head { left: 897px; top: 25px; width: 261px; }
  .frustrations-head { left: 897px; top: 240px; width: 261px; }
  .partners-head { left: 897px; top: 455px; width: 261px; }

  .money-frame {
    position: absolute; left: 287px; top: 25px; width: 608px; height: 611px;
    border-left: 2px solid var(--orange); border-right: 2px solid var(--orange);
    border-radius: 6px 6px 0 0; overflow: hidden;
  }
  .income-col {
    position: absolute; left: 0; top: 0; width: 313px; height: 100%;
    background: linear-gradient(to bottom, var(--income-tint), var(--income-tint-low));
    border-right: 2px solid var(--orange);
  }
  .expense-col {
    position: absolute; left: 315px; top: 0; right: 0; height: 100%;
    background: linear-gradient(to bottom, var(--expense-tint), var(--expense-tint-low));
  }
  .money-head { position: absolute; left: 0; top: 0; width: 100%; height: 41px; background: var(--orange); }
  .income-head { left: 288px; top: 25px; width: 313px; height: 41px; }
  .expenses-head { left: 601px; top: 25px; width: 293px; height: 41px; }

  .balance-bar {
    position: absolute; left: 289px; top: 317px; width: 605px; height: 40px;
    background: var(--orange); border-radius: 0 4px 0 0;
  }
  .assets-head { left: 380px; top: 317px; width: 130px; height: 40px; }
  .debt-head { left: 714px; top: 317px; width: 70px; height: 40px; justify-content: flex-start; }

  .cash-flow { position: absolute; left: 510px; top: 277px; width: 176px; height: 108px; }
  .cash-flow-text {
    position: absolute; left: 510px; top: 277px; width: 176px; height: 108px;
    color: var(--white); font-size: 26px; letter-spacing: 1.2px; line-height: 1.2; text-align: center;
    display: flex; align-items: center; justify-content: center; padding-top: 3px;
  }

  .time-tab { position: absolute; left: 55px; top: 601px; width: 157px; height: 36px; }
  .time-label { left: 55px; top: 606px; width: 128px; height: 30px; }

  .wealth-dome { position: absolute; left: 505px; top: 581px; width: 186px; height: 56px; }
  .wealth-label { left: 505px; top: 603px; width: 186px; height: 30px; }

  .time-band {
    position: absolute; left: 25px; top: 635px; width: 1133px; height: 26px;
    background: var(--blue); border-radius: 6px 6px 0 0;
  }
</style>
</head>
<body>
  <div class="canvas-card"></div>

  <div class="money-frame">
    <div class="income-col"></div>
    <div class="expense-col"></div>
    <div class="money-head"></div>
  </div>

  <div class="label tab-blue goals-head">GOALS</div>
  <div class="label income-head">INCOME</div>
  <div class="label expenses-head">EXPENSES</div>
  <div class="label tab-blue fears-head">FEARS</div>
  <div class="label tab-blue frustrations-head">FRUSTRATIONS</div>
  <div class="label tab-blue partners-head">PARTNERS</div>

  <div class="balance-bar"></div>
  <div class="label assets-head">ASSETS</div>
  <div class="label debt-head">DEBT</div>

  <svg class="cash-flow" viewBox="0 0 176 108" aria-hidden="true">
    <ellipse cx="88" cy="54" rx="85" ry="51" fill="var(--orange)" stroke="var(--orange-ring)" stroke-width="4"/>
  </svg>
  <div class="cash-flow-text">CASH<br>FLOW</div>

  <svg class="time-tab" viewBox="0 0 157 36" aria-hidden="true">
    <path d="M0 36 V8 Q0 0 8 0 H142 Q147 0 149 6 L157 36 Z" fill="var(--blue)"/>
  </svg>
  <svg class="wealth-dome" viewBox="0 0 186 56" aria-hidden="true">
    <path d="M0 56 Q8 0 93 0 Q178 0 186 56 Z" fill="var(--blue)"/>
  </svg>

  <div class="time-band"></div>
  <div class="label time-label">TIME</div>
  <div class="label wealth-label">WEALTH</div>
</body>
</html>
```